Custom Real Estate Instagram stickers

I want to have you design roughly 5 different animated GIFs to use in Instagram stories. The GIFs will have transparent backgrounds and incorporate my logo.
- Here is the list of how I'd like them animated:
- My logo & Moving words "under contract"
- My logo & moving words "just listed"
- My logo & moving words "#sold"
- The lock symbol inside a house with moving words "open house"
- A Heart with Tilden Dwellings Logo inside

Target Market(s)

Homebuyers & Homesellers

Industry/Entity Type

Real Estate

Requirements
Must have
• I'd love to have stickers incorporate houses, for sale signs, moving letters, my logo. Colors that match my logo

```html
<!DOCTYPE html>
<html lang="en">
<head>
<meta charset="utf-8">
<title>Tilden Dwellings – Story Stickers</title>
<link rel="stylesheet" href="https://fonts.googleapis.com/css2?family=Archivo+Black&family=Anton&display=swap">
<style>
  :root {
    --ink: #5b5b5b;
    --teal: #4b7b84;
    --red: #c9141b;
    --red-bright: #e32227;
    --paper: #ffffff;
    --frame: #3a3a3a;
  }
  html, body {
    margin: 0;
    width: 1200px;
    height: 1200px;
    overflow: hidden;
    background: var(--paper);
  }
  .sheet {
    position: relative;
    width: 1200px;
    height: 1200px;
  }
  .sticker {
    position: absolute;
    width: 500px;
    height: 498px;
    box-sizing: border-box;
    border: 1px solid var(--frame);
    background: var(--paper);
  }
  .sticker svg { display: block; width: 100%; height: 100%; }
  .sticker--contract { left: 37px; top: 50px; }
  .sticker--listed   { left: 601px; top: 50px; }
  .sticker--sold     { left: 316px; top: 601px; }

  .brand-name { font-family: "Archivo Black", sans-serif; fill: var(--ink); font-size: 62px; }
  .brand-square { fill: var(--teal); }

  .stamp-contract-box { fill: var(--red); }
  .stamp-contract-text { font-family: "Anton", sans-serif; fill: var(--paper); }
  .listed-just { font-family: "Archivo Black", sans-serif; fill: var(--ink); font-size: 78px; }
  .listed-listed { font-family: "Archivo Black", sans-serif; fill: var(--teal); font-size: 78px; }
  .stamp-sold-frame { fill: none; stroke: var(--red-bright); stroke-width: 9; }
  .stamp-sold-text { font-family: "Archivo Black", sans-serif; fill: var(--red-bright); font-size: 110px; }
</style>
</head>
<body>
<main class="sheet">

  <section class="sticker sticker--contract" aria-label="Under contract sticker">
    <svg viewBox="0 0 500 498" xmlns="http://www.w3.org/2000/svg">
      <g class="brand-name-block">
        <text class="brand-name" x="30" y="150">TILDEN</text>
        <rect class="brand-square" x="420" y="100" width="48" height="48"/>
        <text class="brand-name" x="30" y="240">DWELLINGS</text>
      </g>
      <g class="stamp-contract">
        <rect class="stamp-contract-box" x="72" y="344" width="357" height="121" rx="8"/>
        <text class="stamp-contract-text" x="250" y="402" font-size="56" text-anchor="middle">UNDER</text>
        <text class="stamp-contract-text" x="250" y="455" font-size="50" text-anchor="middle">CONTRACT</text>
      </g>
    </svg>
  </section>

  <section class="sticker sticker--listed" aria-label="Just listed sticker">
    <svg viewBox="0 0 500 498" xmlns="http://www.w3.org/2000/svg">
      <g class="brand-name-block">
        <text class="brand-name" x="30" y="150">TILDEN</text>
        <rect class="brand-square" x="420" y="100" width="48" height="48"/>
        <text class="brand-name" x="30" y="240">DWELLINGS</text>
      </g>
      <g class="listed-words">
        <text class="listed-just" x="33" y="398">JUST</text>
        <text class="listed-listed" x="168" y="465">LISTED</text>
      </g>
    </svg>
  </section>

  <section class="sticker sticker--sold" aria-label="Sold sticker">
    <svg viewBox="0 0 500 498" xmlns="http://www.w3.org/2000/svg">
      <g class="brand-name-block">
        <text class="brand-name" x="30" y="150">TILDEN</text>
        <rect class="brand-square" x="420" y="100" width="48" height="48"/>
        <text class="brand-name" x="30" y="240">DWELLINGS</text>
      </g>
      <g class="stamp-sold" transform="rotate(-3 251 380)">
        <rect class="stamp-sold-frame" x="42" y="322" width="418" height="116" rx="12"/>
        <text class="stamp-sold-text" x="251" y="420" text-anchor="middle">SOLD</text>
      </g>
    </svg>
  </section>

</main>
</body>
</html>
```